Logo für Trockenbauarbeiten aller Art, Spachtelarbeiten und Verputzarbeiten
Zielgruppe
Gegenstand des Unternehmens ist Trockenbauarbeiten aller Art, Spachtelarbeiten und Verputzarbeiten.
Unsere Zielgruppe sind Menschen ab 30 Jahren aufwärts, wir interessieren uns für den einzelnen Hausbesitzer oder Eigentumswohnungbesitzer. Wir benötigen einen hohen Wiedererkennungseffekt.
Wir benötigen Designvorlagen für eine Facebook Seite, Instagram und werden über diese beiden Plattformen auch Werbung schalten, daher benötigen wir dafür auch die verschiedenen Designvorlagen, um verschiedenen Werbekampangen zu erstellen.
Name des Unternehmens: 'WAND-PLAN KOLLHAGEN GmbH'
Aufgabenstellung
Wichtig ist bei den verschiedenen Designs, dass wir Leads bzw. Kundenaufträge sammeln können. Wir müssen herausstechen aus der Masse an Handwerkern. Wir sind die absoluten Spezialisten in unserem Gebiet. Des Weiteren werden wir aus den Materialen diverse Kampagnen erstellen die das komplette Jahr 2022 durchlaufen werden. Vorzugsweise werden wir hierfür die Plattfirm Facebook verwenden, aber auch andere Kanäle.
WICHTIG: Das Logo mit dem roten Haus ist unser original Logo!

```html
<!DOCTYPE html>
<html lang="de">
<head>
<meta charset="utf-8">
<title>WAND-PLAN KOLLHAGEN – Social Post</title>
<link href="https://fonts.googleapis.com/css2?family=Montserrat:wght@700;800&family=Open+Sans:wght@400;600;700&display=swap" rel="stylesheet">
<style>
  :root {
    --bg-dark: #262427;
    --paper: #ffffff;
    --brand-red: #fd0000;
    --ink: #1e1c1d;
    --photo-light: #e9e4dc;
    --photo-warm: #d9c2a2;
  }
  * { margin: 0; padding: 0; box-sizing: border-box; }
  html, body {
    width: 1200px; height: 1200px; overflow: hidden;
    background: var(--bg-dark);
  }
  .post {
    position: relative; width: 1200px; height: 1200px;
    background: var(--bg-dark);
    font-family: "Open Sans", sans-serif;
    color: var(--ink);
  }
  .card {
    position: absolute; left: 104px; top: 104px;
    width: 992px; height: 992px; background: var(--paper);
  }
  .corner-accent {
    position: absolute; left: 104px; top: 104px;
    width: 281px; height: 281px; background: var(--brand-red);
  }
  .hero-photo {
    position: absolute; left: 134px; top: 134px;
    width: 508px; height: 932px;
    background: linear-gradient(100deg, var(--photo-light) 0%, #ece8e2 45%, var(--photo-warm) 100%);
  }
  .brand-name {
    position: absolute; left: 702px; top: 170px; width: 320px;
    font-family: "Montserrat", sans-serif; font-weight: 800;
    font-size: 34px; line-height: 1.05; color: var(--ink);
    letter-spacing: 0.5px;
  }
  .headline {
    position: absolute; left: 696px; top: 300px;
    font-family: "Montserrat", sans-serif; font-weight: 800;
    font-size: 52px; line-height: 64px; color: var(--ink);
  }
  .headline .accent { color: var(--brand-red); }
  .headline-rule {
    position: absolute; left: 697px; top: 511px;
    width: 110px; height: 6px; background: var(--brand-red);
  }
  .intro {
    position: absolute; left: 696px; top: 538px; width: 360px;
    font-size: 20px; line-height: 30px; color: var(--ink);
  }
  .service-box {
    position: absolute; left: 617px; top: 646px;
    width: 479px; height: 303px; background: var(--brand-red);
    color: var(--paper);
  }
  .service-title {
    position: absolute; left: 79px; top: 28px;
    font-family: "Montserrat", sans-serif; font-weight: 800;
    font-size: 42px; line-height: 1;
  }
  .service-list {
    position: absolute; left: 79px; top: 95px; width: 380px;
    list-style: none; font-size: 20.5px; line-height: 30px;
  }
  .service-list li {
    position: relative; padding-left: 30px; margin-bottom: 4px;
  }
  .service-list li::before {
    content: ""; position: absolute; left: 3px; top: 13px;
    width: 9px; height: 9px; border-radius: 50%; background: var(--paper);
  }
  .social {
    position: absolute; left: 153px; top: 997px;
    display: flex; align-items: center; gap: 22px;
  }
  .social-dot {
    width: 46px; height: 46px; border-radius: 50%; background: var(--brand-red);
  }
  .social-handle {
    font-weight: 700; font-size: 29px; color: #3a3838;
  }
  .contact {
    position: absolute; left: 700px; top: 998px;
    display: flex; align-items: center; gap: 20px;
  }
  .contact-icon { width: 50px; height: 50px; }
  .contact-number {
    font-weight: 700; font-size: 40px; color: var(--ink); letter-spacing: 0.5px;
  }
</style>
</head>
<body>
<main class="post">
  <div class="card"></div>
  <div class="corner-accent"></div>
  <div class="hero-photo" role="img" aria-label="Photo of a drywall worker in overalls smoothing filler onto a wall beside a stepladder"></div>

  <div class="brand-name">WAND-PLAN<br>KOLLHAGEN</div>

  <h1 class="headline">Lorem<br><span class="accent">Ipsum dolor</span><br>sit amet</h1>
  <div class="headline-rule"></div>
  <p class="intro">consectetur adipiscing elit, sed do eiusmod tempor incididunt ut labore et dolore magna aliqua.</p>

  <section class="service-box">
    <h2 class="service-title">Our Service</h2>
    <ul class="service-list">
      <li>Lorem ipsum dolor sit amet</li>
      <li>Lorem ipsum dolor sit amet consectetur adipiscing elit</li>
      <li>Lorem ipsum dolor sit amet</li>
      <li>Lorem ipsum dolor sit amet</li>
    </ul>
  </section>

  <div class="social">
    <span class="social-dot"></span>
    <span class="social-handle">Wand_plan_kollhagen</span>
  </div>

  <div class="contact">
    <svg class="contact-icon" viewBox="0 0 50 50" aria-hidden="true">
      <path d="M10 6 C6 8 3 12 4 18 C6 30 18 43 31 46 C37 47 41 44 43 40 L36 33 C34 32 32 33 30 35 C24 33 17 26 15 20 C17 18 18 16 17 14 Z" fill="var(--brand-red)"/>
      <path d="M27 12 A12 12 0 0 1 38 23" fill="none" stroke="var(--brand-red)" stroke-width="3" stroke-linecap="round"/>
      <path d="M28 5 A19 19 0 0 1 45 22" fill="none" stroke="var(--brand-red)" stroke-width="3" stroke-linecap="round"/>
    </svg>
    <span class="contact-number">0160/4817293</span>
  </div>
</main>
</body>
</html>
```